Business Card Design Project

Business Card
We are rebranding with a new logo
Industry/Entity Type
Business
Contact Information for Business Card
Dennis Marlow +61 427581962 dennis@qovo.com.au P.O. Box 872 Kelvindale QLD 4309
Requirements
Must have
- Logo

```html
<!DOCTYPE html>
<html lang="en">
<head>
<meta charset="utf-8">
<title>Qovo International – Business Card</title>
<link rel="stylesheet" href="https://fonts.googleapis.com/css2?family=Exo+2:wght@400;600&display=swap">
<style>
  :root {
    --backdrop: #e4e4e4;
    --card: #ffffff;
    --blue-deep: #074a6e;
    --blue-bright: #0a9ad6;
    --brand-blue: #0b7fbf;
    --accent-orange: #f08a24;
    --ink-light: #ffffff;
    --ink-grey: #9a9a9a;
  }
  * { margin: 0; padding: 0; box-sizing: border-box; }
  html, body {
    width: 1200px;
    height: 1000px;
    overflow: hidden;
    background: var(--backdrop);
    font-family: "Exo 2", sans-serif;
  }
  .business-card {
    position: absolute;
    left: 120px;
    top: 225px;
    width: 960px;
    height: 550px;
    background: var(--card);
    box-shadow: 0 6px 18px rgba(0, 0, 0, 0.18);
    overflow: hidden;
  }
  .side-panel {
    position: absolute;
    inset: 0;
    width: 100%;
    height: 100%;
  }
  .holder-name {
    position: absolute;
    left: 70px;
    top: 84px;
    color: var(--ink-light);
    font-size: 21px;
    font-weight: 400;
    line-height: 28px;
    letter-spacing: 0.5px;
    text-transform: uppercase;
  }
  .brand-name {
    position: absolute;
    right: 74px;
    top: 96px;
    text-align: right;
    color: var(--brand-blue);
    font-weight: 600;
  }
  .brand-name .brand-word {
    display: block;
    font-size: 58px;
    line-height: 62px;
    letter-spacing: 2px;
  }
  .brand-name .brand-tag {
    display: block;
    font-size: 18px;
    letter-spacing: 3px;
    margin-top: 8px;
  }
  .contact-list {
    position: absolute;
    right: 73px;
    top: 390px;
    list-style: none;
    text-align: right;
    color: var(--ink-grey);
    font-size: 19px;
    line-height: 30px;
    letter-spacing: 1px;
  }
</style>
</head>
<body>
  <section class="business-card">
    <svg class="side-panel" viewBox="0 0 960 550" preserveAspectRatio="none" aria-hidden="true">
      <defs>
        <linearGradient id="panelBlue" x1="0" y1="0" x2="1" y2="0">
          <stop offset="0" style="stop-color: #074a6e"/>
          <stop offset="1" style="stop-color: #0a9ad6"/>
        </linearGradient>
      </defs>
      <polygon class="accent-line" fill="#f08a24" points="0,0 556,0 126,550 0,550"/>
      <polygon class="panel-blue" fill="url(#panelBlue)" points="0,0 544,0 114,550 0,550"/>
    </svg>

    <h1 class="holder-name">Dennis<br>Marlow</h1>

    <div class="brand-name">
      <span class="brand-word">Qovo</span>
      <span class="brand-tag">INTERNATIONAL</span>
    </div>

    <ul class="contact-list">
      <li>+61 427581962</li>
      <li>dennis@qovo.com.au</li>
      <li>P.O. Box 872 Kelvindale QLD 4309</li>
    </ul>
  </section>
</body>
</html>
```